Wirenexa

I'm looking to much improve our current website wirenexa.com
Updates

Low design quality

Target Market(s)

Commercial clients (Not-Residentials)

Industry/Entity Type

Office buildings and Industrial clients

Coding

Coded - Design and coding required

Number of Pages Required

5+ page

Requirements
Must have
• Very professional structured low voltage cabling projects for Wi-Fi, Audio/Video conference rooms, Access Control systems, CCTV.

```html
<!DOCTYPE html>
<html lang="en">
<head>
<meta charset="utf-8">
<title>Wirenexa — Professional Cabling Solutions</title>
<link href="https://fonts.googleapis.com/css2?family=Poppins:wght@400;500;600;700&display=swap" rel="stylesheet">
<style>
:root{
  --red:#e3302f;
  --red-bright:#ea3439;
  --ink:#161a22;
  --body:#5a5f6a;
  --muted:#8a8f99;
  --line:#e6e8ec;
  --blush:#fbf3f3;
  --field:#eef3fb;
  --black:#050505;
  --white:#ffffff;
}
*{box-sizing:border-box;margin:0;padding:0}
html,body{width:1200px;height:5089px;overflow:hidden}
body{font-family:'Poppins',sans-serif;color:var(--ink);background:var(--white);position:relative}
.abs{position:absolute}
a{color:inherit;text-decoration:none}

/* nav */
.nav{top:0;left:0;width:1200px;height:82px;background:var(--white);border-bottom:1px solid var(--line)}
.brand{display:flex;align-items:center;gap:8px;font-weight:700;font-size:30px;color:var(--ink);letter-spacing:-.5px}
.brand-mark{width:28px;height:28px;background:var(--red);border-radius:3px}
.nav .brand{position:absolute;left:74px;top:20px}
.nav-links{position:absolute;left:474px;top:31px;display:flex;gap:42px;font-size:13px;color:#333}
.nav-phone{position:absolute;left:840px;top:30px;display:flex;gap:8px;align-items:center;font-size:13px;color:var(--red);font-weight:500}
.btn{display:inline-flex;align-items:center;justify-content:center;gap:8px;background:var(--red);color:var(--white);font-weight:600;border-radius:24px}
.nav .btn{position:absolute;left:992px;top:18px;width:134px;height:44px;font-size:12px;letter-spacing:.5px}

/* hero */
.hero{top:82px;left:0;width:1200px;height:706px;background:radial-gradient(ellipse at 75% 35%,#3d4a4f 0%,#1c2427 45%,#0b0f11 100%)}
.hero-photo{position:absolute;inset:0;background:linear-gradient(90deg,rgba(8,10,12,.85) 0%,rgba(8,10,12,.55) 50%,rgba(30,60,70,.35) 100%)}
.badge{position:absolute;left:73px;top:165px;background:var(--red);color:var(--white);font-size:11px;letter-spacing:1.3px;padding:5px 10px;border-radius:14px}
.hero h1{position:absolute;left:72px;top:208px;width:600px;font-size:55px;line-height:60px;font-weight:700;color:var(--white);letter-spacing:-.5px}
.hero-lede{position:absolute;left:73px;top:413px;width:450px;font-size:14px;line-height:23px;color:#e4e6ea}
.hero-cta{position:absolute;left:73px;top:543px;width:206px;height:46px;font-size:12px}
.years{position:absolute;left:292px;top:543px;width:234px;height:48px;border:1px solid rgba(255,255,255,.3);border-radius:10px;background:rgba(0,0,0,.3);display:flex;align-items:center;gap:12px;padding-left:18px;color:var(--white);font-size:12px}
.years-box{width:30px;height:30px;background:var(--white);border-radius:4px}
.callback{position:absolute;left:759px;top:124px;width:366px;height:498px;background:var(--white);border-radius:12px;padding:36px 34px}
.callback h3{font-size:23px;font-weight:600}
.callback .hint{font-size:12px;color:var(--muted);margin-top:8px;line-height:19px}
.lbl{display:block;font-size:12px;color:#444;margin-top:20px;margin-bottom:7px}
.inp{border:1px solid var(--line);border-radius:4px;height:40px;font-size:12px;color:var(--muted);padding:10px 10px;white-space:nowrap;overflow:hidden}
.row2{display:flex;gap:14px}
.row2>div{flex:1;min-width:0}
.callback .area{height:80px;white-space:normal}
.callback .btn{width:100%;height:46px;border-radius:6px;font-size:13px;margin-top:16px}

/* about */
.about h2{position:absolute;left:72px;top:906px;font-size:33px;line-height:46px;font-weight:600}
.see-more{position:absolute;left:994px;top:943px;width:131px;height:43px;font-size:12px}
.about-photo{position:absolute;left:73px;top:1032px;width:437px;height:476px;border-radius:18px;background:linear-gradient(135deg,#9aa2a4 0%,#5e6b6e 40%,#b63a32 70%,#6d2a28 100%)}
.about-text{position:absolute;left:553px;top:1032px;width:580px;font-size:14px;line-height:25px;color:var(--body)}
.feat-grid{position:absolute;left:553px;top:1131px;width:572px;display:grid;grid-template-columns:1fr 1fr;gap:25px 18px}
.feat{height:109px;border:1px solid var(--line);border-radius:10px;box-shadow:0 3px 10px rgba(0,0,0,.05);padding:18px 16px;display:flex;gap:12px}
.feat-ico{flex:0 0 30px;height:30px;border-radius:50%;background:#fde8e8;display:flex;align-items:center;justify-content:center}
.feat h4{font-size:12px;font-weight:600;margin-bottom:5px}
.feat p{font-size:10.5px;line-height:16px;color:var(--body)}
.feat ul{list-style:none;font-size:11px;line-height:22px;padding-left:4px;padding-top:8px}
.feat li::before{content:"";display:inline-block;width:5px;height:5px;background:var(--red);border-radius:50%;margin-right:12px;vertical-align:middle}

/* strategic */
.strategic{top:1620px;left:0;width:1200px;height:768px;background:var(--blush)}
.sec-title{text-align:center;font-size:33px;font-weight:600}
.strategic .sec-title{position:absolute;top:80px;width:100%}
.strategic .sub{position:absolute;top:142px;width:100%;text-align:center;font-size:13px;color:var(--body)}
.svc{position:absolute;top:199px;width:338px;background:var(--white);border-radius:10px;overflow:hidden;box-shadow:0 4px 14px rgba(0,0,0,.05)}
.svc-img{height:213px}
.svc-body{padding:32px 26px 40px}
.svc h3{font-size:17px;font-weight:600;margin-bottom:16px}
.svc p{font-size:13px;line-height:20px;color:var(--body)}
.svc a{display:block;margin-top:22px;color:var(--red);font-size:12px;font-weight:600}

/* why */
.why{top:2388px;left:0;width:1200px;height:480px;background:var(--red-bright);color:var(--white)}
.why .sec-title{position:absolute;top:66px;width:100%}
.why p{position:absolute;left:180px;top:128px;width:840px;text-align:center;font-size:14px;line-height:25px}
.why-box{position:absolute;left:235px;top:214px;width:730px;height:172px;background:var(--white);border-radius:12px;display:flex;justify-content:space-around;padding:0 60px;align-items:center}
.why-item{text-align:center;color:var(--red);font-size:19px;font-weight:500}
.why-ico{width:58px;height:58px;border-radius:50%;background:var(--red);margin:0 auto 18px;display:flex;align-items:center;justify-content:center}

/* capabilities */
.caps h2{position:absolute;left:113px;top:2972px;font-size:33px;font-weight:600}
.caps .sub{position:absolute;left:113px;top:3036px;width:420px;font-size:13px;line-height:20px;color:#333}
.cap{position:absolute;width:300px;height:266px;border:2px solid var(--red);border-radius:14px;padding:40px 34px}
.cap-ico{width:38px;height:38px;background:var(--red);border-radius:6px;display:flex;align-items:center;justify-content:center;margin-bottom:28px}
.cap h3{font-size:20px;font-weight:500;line-height:27px;margin-bottom:26px}
.cap p{font-size:13px;line-height:21px;color:var(--body)}

/* contact */
.contact{top:3780px;left:0;width:1200px;height:790px;background:#fbf6f6}
.contact-card{position:absolute;left:132px;top:103px;width:934px;height:589px;background:var(--white);border-radius:8px;box-shadow:0 10px 30px rgba(0,0,0,.08);display:flex;overflow:hidden}
.contact-side{width:390px;background:var(--red-bright);color:var(--white);padding:54px 52px}
.contact-side h2{font-size:41px;line-height:41px;font-weight:600}
.contact-side .intro{font-size:13px;line-height:20px;margin-top:32px;width:230px;opacity:.95}
.info{display:flex;gap:16px;margin-top:30px}
.info-ico{flex:0 0 26px;height:26px;border-radius:5px;background:rgba(255,255,255,.2);display:flex;align-items:center;justify-content:center}
.info small{display:block;font-size:11px;letter-spacing:1.5px;opacity:.85;margin-bottom:4px}
.info span{font-size:14px;font-weight:500;line-height:21px}
.contact-form{flex:1;padding:54px 52px}
.contact-form .kicker{font-size:12px}
.contact-form .lbl{margin-top:36px}
.contact-form .fld{height:46px;background:var(--field);border-radius:3px}
.contact-form .big{height:138px}
.contact-form .btn{width:100%;height:52px;border-radius:6px;font-size:13px;margin-top:32px}

/* footer */
.footer{top:4570px;left:0;width:1200px;height:519px;background:var(--black);color:#d8d8d8}
.footer .brand{position:absolute;left:74px;top:108px;color:var(--white)}
.footer .about-co{position:absolute;left:74px;top:162px;width:330px;font-size:12px;line-height:21px}
.socials{position:absolute;left:74px;top:279px;display:flex;gap:16px}
.socials span{width:32px;height:32px;border-radius:50%;background:var(--red)}
.fcol{position:absolute;top:110px;font-size:13px;line-height:33px}
.fcol h5{color:var(--red);font-size:12px;font-weight:600;margin-bottom:6px;line-height:20px}
.fcol a{display:block}
.footer hr{position:absolute;left:0;top:396px;width:1200px;border:0;border-top:1px solid #2a2a2a}
.copy{position:absolute;top:450px;width:100%;text-align:center;font-size:11px}
</style>
</head>
<body>

<header class="nav abs">
  <div class="brand"><span class="brand-mark"></span>Wirenexa</div>
  <nav class="nav-links"><a>Home</a><a>About Us</a><a>Services</a></nav>
  <div class="nav-phone">
    <svg width="14" height="14" viewBox="0 0 24 24" fill="none" stroke="currentColor" stroke-width="2"><path d="M22 16.9v3a2 2 0 0 1-2.2 2 19.8 19.8 0 0 1-8.6-3.1 19.5 19.5 0 0 1-6-6A19.8 19.8 0 0 1 2.1 4.2 2 2 0 0 1 4.1 2h3a2 2 0 0 1 2 1.7c.1.9.4 1.8.7 2.7a2 2 0 0 1-.5 2.1L8 9.8a16 16 0 0 0 6 6l1.3-1.3a2 2 0 0 1 2.1-.4c.9.3 1.8.6 2.7.7a2 2 0 0 1 1.7 2z"/></svg>
    (800)-555-0142
  </div>
  <a class="btn">CONTACT</a>
</header>

<section class="hero abs">
  <div class="hero-photo" role="img" aria-label="Server rack with bundles of network patch cables"></div>
  <span class="badge">SERVING VA, DC &amp; MD</span>
  <h1>Professional Cabling Solutions for Enterprise</h1>
  <p class="hero-lede">Expert low voltage cabling for Wi-Fi, AV conference rooms, Access Control and CCTV. Delivering structural precision across the tri-state area with 30 years of industrial excellence.</p>
  <a class="btn hero-cta">EXPLORE SERVICES
    <svg width="12" height="12" viewBox="0 0 24 24" fill="none" stroke="#fff" stroke-width="3"><path d="M5 12h14M13 6l6 6-6 6"/></svg></a>
  <div class="years"><span class="years-box"></span>30 Years of Excellence</div>
  <form class="callback">
    <h3>Request Callback</h3>
    <p class="hint">Submit details and we'll contact you within 1 hour.</p>
    <label class="lbl">Full Name</label>
    <div class="inp">Your Name</div>
    <div class="row2">
      <div><label class="lbl">Email</label><div class="inp">email@company.com</div></div>
      <div><label class="lbl">Phone</label><div class="inp">(555) 000-0000</div></div>
    </div>
    <label class="lbl" style="margin-top:10px">Project Needs</label>
    <div class="inp area">Tell us about your infrastructure goals...</div>
    <a class="btn">Submit Request</a>
  </form>
</section>

<section class="about">
  <h2>Elevate Your Connectivity<br>with Wirenexa</h2>
  <a class="btn see-more">SEE MORE</a>
  <div class="about-photo" role="img" aria-label="Technician in red hard hat working at an electrical cabinet"></div>
  <p class="about-text">Wirenexa is your premier provider of professional low voltage cabling services. We prioritize quality, reliability, and architectural precision to deliver exceptional infrastructure for modern business demands.</p>
  <div class="feat-grid">
    <div class="feat"><span class="feat-ico"><svg width="14" height="14" viewBox="0 0 24 24" fill="none" stroke="#e3302f" stroke-width="2.5"><circle cx="12" cy="12" r="9"/><path d="M8 12l3 3 5-6"/></svg></span>
      <div><h4>Expertise and Experience</h4><p>Decades of industrial experience handling small offices to large-scale data centers</p></div></div>
    <div class="feat"><span class="feat-ico"><svg width="14" height="14" viewBox="0 0 24 24" fill="none" stroke="#e3302f" stroke-width="2.5"><path d="M6 3v18M12 3v18M18 3v18"/></svg></span>
      <div><h4>Comprehensive Solutions</h4><p>From Copper CAT6 to high-density Fiber Optics, we cover every technical requirement.</p></div></div>
    <div class="feat"><span class="feat-ico"><svg width="14" height="14" viewBox="0 0 24 24" fill="none" stroke="#e3302f" stroke-width="2.5"><path d="M7 20l5-16 5 16"/></svg></span>
      <div><h4>Quality Workmanship</h4><p>From copper CAT6 and CAT7 cabling to fiber optic installations (single and multimode)</p></div></div>
    <div class="feat"><span class="feat-ico"><svg width="14" height="14" viewBox="0 0 24 24" fill="none" stroke="#e3302f" stroke-width="2.5"><rect x="4" y="6" width="16" height="12" rx="2"/></svg></span>
      <div><h4>Commercial and Industrial</h4><p>Built for office buildings, plants and industrial facilities.</p></div></div>
    <div class="feat"><span class="feat-ico"><svg width="14" height="14" viewBox="0 0 24 24" fill="none" stroke="#e3302f" stroke-width="2.5"><path d="M12 3v4M12 17v4M3 12h4M17 12h4"/></svg></span>
      <div><h4>Customer Satisfaction</h4><p>Our commitment to customer satisfaction drives everything we do.</p></div></div>
    <div class="feat"><ul><li>Wi-Fi &amp; AV Conference Rooms</li><li>Access Control Systems</li><li>CCTV Surveillance</li></ul></div>
  </div>
</section>

<section class="strategic abs">
  <h2 class="sec-title">Strategic Infrastructure</h2>
  <p class="sub">Focused cabling expertise tailored to your specific environment and technical scale.</p>
  <article class="svc" style="left:63px">
    <div class="svc-img" role="img" aria-label="Modern corporate office building exterior" style="background:linear-gradient(160deg,#8fb2d6 0%,#c9ccd0 45%,#4a4d52 100%)"></div>
    <div class="svc-body"><h3>Office Buildings</h3><p>Wi-Fi, AV conference rooms, access control and CCTV cabling for multi-tenant office buildings.</p><a>Contact Now ›</a></div>
  </article>
  <article class="svc" style="left:425px">
    <div class="svc-img" role="img" aria-label="Retail store interior" style="background:linear-gradient(160deg,#3a3a3d 0%,#b44a45 55%,#e7e2dc 100%)"></div>
    <div class="svc-body"><h3>Commercial Services</h3><p>Complete office low voltage systems, Wi-Fi networks, and integrated security for high-density environments.</p><a>Contact Now ›</a></div>
  </article>
  <article class="svc" style="left:787px">
    <div class="svc-img" role="img" aria-label="Industrial power plant at dusk" style="background:linear-gradient(180deg,#5d6470 0%,#2e3440 55%,#1a1f2a 100%)"></div>
    <div class="svc-body"><h3>Industrial Services</h3><p>Structured cabling, IDF and MDF for manufacturing, distribution centers, and mission-critical facilities.</p><a>Contact Now ›</a></div>
  </article>
</section>

<section class="why abs">
  <h2 class="sec-title">Why Choose Us</h2>
  <p>Wirenexa is your premier provider of professional low voltage cabling services. We prioritize quality, reliability, and architectural precision to deliver exceptional infrastructure for modern business demands.</p>
  <div class="why-box">
    <div class="why-item"><div class="why-ico"><svg width="24" height="24" viewBox="0 0 24 24" fill="none" stroke="#fff" stroke-width="2"><path d="M12 3l7 3v6c0 4-3 7-7 9-4-2-7-5-7-9V6z"/></svg></div>Safe &amp; Secure</div>
    <div class="why-item"><div class="why-ico"><svg width="24" height="24" viewBox="0 0 24 24" fill="none" stroke="#fff" stroke-width="2"><path d="M4 15v-3a8 8 0 0 1 16 0v3"/><rect x="3" y="14" width="4" height="6" rx="1"/><rect x="17" y="14" width="4" height="6" rx="1"/></svg></div>24x7 Support</div>
    <div class="why-item"><div class="why-ico"><svg width="24" height="24" viewBox="0 0 24 24" fill="none" stroke="#fff" stroke-width="2"><rect x="5" y="4" width="14" height="16" rx="2"/><path d="M12 8v8M9.5 10h4a1.5 1.5 0 0 1 0 3h-3a1.5 1.5 0 0 0 0 3h4"/></svg></div>Low Cost</div>
  </div>
</section>

<section class="caps">
  <h2>Core Capabilities</h2>
  <p class="sub">Technically rigorous services designed to meet international engineering standards.</p>
  <div class="cap" style="left:113px;top:3106px"><div class="cap-ico"><svg width="20" height="20" viewBox="0 0 24 24" fill="none" stroke="#fff" stroke-width="2"><path d="M8 8l-4 4 4 4M16 8l4 4-4 4"/></svg></div><h3>Voice &amp; Data Cable</h3><p>Precision installation for high-speed local area networks and VOIP systems.</p></div>
  <div class="cap" style="left:443px;top:3106px"><div class="cap-ico"><svg width="20" height="20" viewBox="0 0 24 24" fill="none" stroke="#fff" stroke-width="2"><rect x="3" y="5" width="18" height="12" rx="1"/><path d="M8 21h8M12 17v4"/></svg></div><h3>AV Conference Rooms</h3><p>Display, audio and video cabling for boardrooms and meeting spaces.</p></div>
  <div class="cap" style="left:787px;top:3106px"><div class="cap-ico"><svg width="20" height="20" viewBox="0 0 24 24" fill="none" stroke="#fff" stroke-width="2"><rect x="9" y="3" width="6" height="5"/><rect x="3" y="16" width="6" height="5"/><rect x="15" y="16" width="6" height="5"/><path d="M12 8v4M6 16v-4h12v4"/></svg></div><h3>Fiber Single/Multi Mode</h3><p>High-bandwidth backbone cabling for data centers and campus connectivity</p></div>
  <div class="cap" style="left:113px;top:3406px"><div class="cap-ico"><svg width="20" height="20" viewBox="0 0 24 24" fill="none" stroke="#fff" stroke-width="2"><rect x="6" y="10" width="12" height="10" rx="1"/><path d="M9 10V7a3 3 0 0 1 6 0v3"/></svg></div><h3>Access Control</h3><p>Card reader, door lock and entry system cabling for secure facilities.</p></div>
  <div class="cap" style="left:443px;top:3406px"><div class="cap-ico"><svg width="20" height="20" viewBox="0 0 24 24" fill="none" stroke="#fff" stroke-width="2"><rect x="3" y="7" width="13" height="8" rx="1"/><path d="M16 10l5-2v6l-5-2M8 15v5"/></svg></div><h3>CCTV Systems</h3><p>IP camera cabling and PoE runs for full-coverage video surveillance.</p></div>
  <div class="cap" style="left:787px;top:3406px"><div class="cap-ico"><svg width="20" height="20" viewBox="0 0 24 24" fill="none" stroke="#fff" stroke-width="2"><path d="M6 20h12M9 20v-6l5-8 3 2-5 8"/></svg></div><h3>Tracemark Testing</h3><p>Industry-leading testing (TX-9000) to guarantee performance compliance.</p></div>
</section>

<section class="contact abs">
  <div class="contact-card">
    <div class="contact-side">
      <h2>Let's Secure Your Infrastructure</h2>
      <p class="intro">Ready to upgrade your enterprise network? Get in touch for a comprehensive technical assessment and quote today.</p>
      <div class="info"><span class="info-ico"><svg width="12" height="12" viewBox="0 0 24 24" fill="#fff"><path d="M6 2l4 4-2 3a12 12 0 0 0 7 7l3-2 4 4-3 4C10 21 3 14 2 5z"/></svg></span><div><small>LOCAL SUPPORT</small><span>(703) 555-0186</span></div></div>
      <div class="info"><span class="info-ico"><svg width="12" height="12" viewBox="0 0 24 24" fill="none" stroke="#fff" stroke-width="2.5"><rect x="3" y="5" width="18" height="14"/><path d="M3 6l9 7 9-7"/></svg></span><div><small>EMAIL SALES</small><span>sales@wirenexa.com</span></div></div>
      <div class="info"><span class="info-ico"><svg width="12" height="12" viewBox="0 0 24 24" fill="none" stroke="#fff" stroke-width="2.5"><path d="M12 22s7-7 7-12a7 7 0 0 0-14 0c0 5 7 12 7 12z"/><circle cx="12" cy="10" r="2.5"/></svg></span><div><small>HEADQUARTERS</small><span>4150 Harbor Point Dr, Suite 310<br>Fairhill, VA 22150</span></div></div>
    </div>
    <form class="contact-form">
      <p class="kicker">Request a Quote Today</p>
      <div class="row2" style="gap:30px">
        <div><label class="lbl">First Name</label><div class="fld"></div></div>
        <div><label class="lbl">Last Name</label><div class="fld"></div></div>
      </div>
      <label class="lbl">Company Phone</label><div class="fld"></div>
      <label class="lbl">Project Details</label><div class="fld big"></div>
      <a class="btn">Send Quote Request</a>
    </form>
  </div>
</section>

<footer class="footer abs">
  <div class="brand"><span class="brand-mark"></span>Wirenexa</div>
  <p class="about-co">A local group of IT professionals dedicated to fast, reliable and honest infrastructure service. No job is too big or too small for our expert engineering team.</p>
  <div class="socials"><span></span><span></span><span></span><span></span><span></span></div>
  <div class="fcol" style="left:453px"><h5>Solutions</h5><a>Fiber Optic Cabling</a><a>AV Conference Rooms</a><a>Access Control</a><a>CCTV Systems</a><a>Structured Cabling</a></div>
  <div class="fcol" style="left:702px"><h5>Useful Links</h5><a>Home</a><a>About Us</a><a>Services</a><a>Contact</a></div>
  <div class="fcol" style="left:913px"><h5>Company</h5><a>About Wirenexa</a><a>Case Studies</a><a>Careers</a><a>Privacy Policy</a><a>Contact Us</a></div>
  <hr>
  <p class="copy">© 2026 Wirenexa. All rights reserved.</p>
</footer>

</body>
</html>
```